The tide parlor saltwater aquarium store business card

Looking for a serious business card for a saltwater fish and coral store. I want this thing to blow people's minds when they see it. I would like the card to look very professional but I also want people to know what the tide parlor is just by seeing the card. Iam pretty open to anything as long as it's one of a kind.

Industry/Entity Type

Business

Contact Information for Business Card

18735 Calder highway Ashbrook pa 16148. Thetideparlor.com. Customerservice@thetideparlor.com. 5038826417

Requirements
Should not have
• Please no child like fish designs

```html
<!DOCTYPE html>
<html lang="en">
<head>
<meta charset="utf-8">
<title>The Tide Parlor – Business Card</title>
<link rel="stylesheet" href="https://fonts.googleapis.com/css2?family=Lato:wght@400;700;900&display=swap">
<style>
  :root {
    --page-bg: #1a1a1a;
    --card-bg: #0b0b0c;
    --card-edge: #1f1f22;
    --accent: #5ab0e8;
    --frame: #6f7fe0;
    --text-main: #f2f2f2;
    --text-soft: #d6d6d6;
    --divider: #9aa8ff;
  }
  * { box-sizing: border-box; margin: 0; padding: 0; }
  html, body { width: 1200px; height: 864px; overflow: hidden; }
  body {
    background: var(--page-bg);
    font-family: "Lato", Arial, sans-serif;
    display: flex;
    align-items: center;
    justify-content: center;
    gap: 60px;
  }
  .card {
    position: relative;
    width: 525px;
    height: 300px;
    background: linear-gradient(160deg, #151517 0%, var(--card-bg) 55%, #050505 100%);
    border: 1px solid var(--card-edge);
    box-shadow: 0 20px 40px rgba(0,0,0,0.55);
    overflow: hidden;
  }

  /* Front */
  .tab {
    position: absolute;
    height: 12px;
    background: var(--accent);
    border-radius: 6px;
  }
  .tab--top { top: -6px; left: 310px; width: 170px; }
  .tab--bottom { bottom: -6px; left: 245px; width: 185px; }
  .divider {
    position: absolute;
    left: 300px; top: 48px;
    width: 1px; height: 206px;
    background: var(--divider);
    opacity: 0.8;
  }
  .contact {
    position: absolute;
    left: 46px; top: 62px;
    color: var(--text-soft);
  }
  .contact__name {
    font-weight: 900;
    font-size: 17px;
    letter-spacing: 0.5px;
    color: var(--text-main);
  }
  .contact__title {
    font-size: 11px;
    letter-spacing: 0.8px;
    color: var(--accent);
    margin-top: 2px;
    margin-bottom: 22px;
  }
  .contact__list { list-style: none; }
  .contact__item {
    display: flex;
    align-items: center;
    gap: 8px;
    font-size: 12px;
    line-height: 21px;
  }
  .contact__item svg { width: 12px; height: 12px; fill: var(--text-soft); flex: none; }
  .contact__address {
    font-size: 12px;
    line-height: 16px;
    margin-top: 6px;
  }
  .brand {
    position: absolute;
    display: flex;
    align-items: center;
    gap: 10px;
    color: var(--accent);
    font-weight: 900;
    white-space: nowrap;
  }
  .brand__dot {
    width: 14px; height: 14px;
    border-radius: 50%;
    background: var(--accent);
    flex: none;
  }
  .card--front .brand { left: 322px; top: 136px; font-size: 22px; }

  /* Back */
  .frame {
    position: absolute;
    inset: 18px;
    border: 1.5px solid var(--frame);
  }
  .card--back .brand {
    left: 50%; top: 50%;
    transform: translate(-50%, -50%);
    font-size: 36px;
  }
  .url-tab {
    position: absolute;
    left: 18px; bottom: 8px;
    padding: 4px 12px;
    background: var(--card-bg);
    border: 1.5px solid var(--frame);
    color: var(--text-soft);
    font-size: 11px;
    letter-spacing: 0.3px;
  }
</style>
</head>
<body>

  <section class="card card--front" aria-label="Business card front">
    <span class="tab tab--top"></span>
    <span class="tab tab--bottom"></span>

    <div class="contact">
      <p class="contact__name">MARCUS HALE</p>
      <p class="contact__title">PRESIDENT</p>
      <ul class="contact__list">
        <li class="contact__item">
          <svg viewBox="0 0 24 24" aria-hidden="true"><path d="M6.6 10.8a15.1 15.1 0 0 0 6.6 6.6l2.2-2.2a1 1 0 0 1 1-.25 11.4 11.4 0 0 0 3.6.57 1 1 0 0 1 1 1V20a1 1 0 0 1-1 1A17 17 0 0 1 3 4a1 1 0 0 1 1-1h3.5a1 1 0 0 1 1 1c0 1.25.2 2.45.57 3.6a1 1 0 0 1-.25 1z"/></svg>
          503-882-6417
        </li>
        <li class="contact__item">
          <svg viewBox="0 0 24 24" aria-hidden="true"><path d="M2 5h20v14H2zm2 2v.4l8 5 8-5V7zm0 2.8V17h16V9.8l-8 5z"/></svg>
          Customerservice@thetideparlor.com
        </li>
        <li class="contact__item">
          <svg viewBox="0 0 24 24" aria-hidden="true"><path d="M12 2a10 10 0 1 0 0 20 10 10 0 0 0 0-20zm6.9 9h-3a15 15 0 0 0-1.3-5.6A8 8 0 0 1 18.9 11zM12 4c.9 1.2 1.8 3.6 1.9 7h-3.8c.1-3.4 1-5.8 1.9-7zM9.4 5.4A15 15 0 0 0 8.1 11h-3a8 8 0 0 1 4.3-5.6zM5.1 13h3a15 15 0 0 0 1.3 5.6A8 8 0 0 1 5.1 13zM12 20c-.9-1.2-1.8-3.6-1.9-7h3.8c-.1 3.4-1 5.8-1.9 7zm2.6-1.4a15 15 0 0 0 1.3-5.6h3a8 8 0 0 1-4.3 5.6z"/></svg>
          www.thetideparlor.com
        </li>
      </ul>
      <p class="contact__address">18735 Calder highway,<br>Ashbrook pa 16148</p>
    </div>

    <span class="divider"></span>

    <div class="brand">
      <span class="brand__dot"></span>
      The Tide Parlor
    </div>
  </section>

  <section class="card card--back" aria-label="Business card back">
    <span class="frame"></span>
    <div class="brand">
      <span class="brand__dot"></span>
      The Tide Parlor
    </div>
    <span class="url-tab">www.thetideparlor.com</span>
  </section>

</body>
</html>
```